Logo & Visitenkarte für Schreinermonteur (Fenster und Türen)
Sehr gute Designerin, gute Ideen und sie hat alle Änderungswünsche sehr schnell und genau umgesetzt. Jederzeit gerne wieder!
Zielgruppe
Verkauf und Einbau von Fenster und Türen (Bauelemente). Meine Zielgruppen sind Menschen, die ein Haus bauen oder renovieren und Fenster und Türen benötigen. Ich mache die Berautung und baue anschliessend die Türen, Fenster und Jalousien auch mit meinem Team ein.
Aufgabenstellung
Ich bin selbständiger Schreiner im Südschwarzwald und derzeit auf den Einbau von Fenster und Türen spezialisiert. Ich möchte meine Initialien KM in meinem Logo enthalten haben, bin aber auch offen für andere Vorschläge. Derzeit bin ich unter 'KM Holzmontagen' bekannt.
Gerne darf als Untertitel 'Fenster und Türen' verwendet werden. Da ich die Option haben möchte, dass ich das Logo/meine Initialien weiterverwende, aber meine Spezialisierung von 'Fenster und Türen' ändere, sollte dies zwar im Logo enthalten sein, aber nicht zu stark integriert sein.
Ich arbeite in einer ländlichen Gegend und das Logo sollte Zuverlässigkeit, Flexibilität und Individualität ausstrahlen und einen hohen Widererkennungswert haben, da es viele andere Schreiner hier gibt. Ich bin bekannt für meine exakte und qualitativ hochwertige Arbeit und bin auch ein Spezialist, wenn es um die Beratung meiner Kunden bei der Fenster und Türenauswahl geht.
Bei den Farben bin ich noch etwas unentschlossen. Derzeit habe ich grau-blau als Farben, bin aber offen für andere Vorschläge. Nur bitte kein rot/rosa. Falls Fragen sind, bitte einfach kurz schreiben.
Besten Dank vorab für die Vorschläge!

```html
<!DOCTYPE html>
<html lang="de">
<head>
<meta charset="utf-8">
<title>KMayer – Visitenkarten</title>
<link rel="stylesheet" href="https://fonts.googleapis.com/css2?family=Roboto:wght@400;700&display=swap">
<style>
  :root {
    --stage: #00121b;
    --navy: #04046a;
    --paper: #ffffff;
    --ink: #111111;
  }
  * { margin: 0; padding: 0; box-sizing: border-box; }
  html, body { width: 1200px; height: 817px; overflow: hidden; background: var(--stage); }
  body { position: relative; font-family: "Roboto", Arial, sans-serif; color: var(--ink); }

  .card { position: absolute; width: 492px; height: 319px; background: var(--paper); overflow: hidden; }
  .card--front-light { left: 97px; top: 83px; }
  .card--front-dark  { left: 611px; top: 83px; background: var(--navy); }
  .card--back-a { left: 97px; top: 415px; }
  .card--back-b { left: 611px; top: 415px; }

  .wordmark { font-weight: 700; color: var(--navy); letter-spacing: 0.5px; line-height: 1; }
  .card--front-dark .wordmark { color: var(--paper); }

  .front-logo { position: absolute; left: 0; right: 0; top: 140px; text-align: center; font-size: 42px; }
  .front-web { position: absolute; left: 0; right: 0; top: 281px; text-align: center; font-size: 13.5px; color: var(--navy); }
  .card--front-dark .front-web { color: var(--paper); }

  .rule { position: absolute; left: 61px; width: 3px; background: var(--navy); }
  .rule--top { top: 0; height: 36px; }
  .rule--bottom { top: 123px; bottom: 0; }

  .back-logo { position: absolute; left: 38px; top: 57px; }
  .back-logo .wordmark { font-size: 36px; }
  .tagline { display: block; margin-top: 6px; padding-left: 32px; font-size: 11px; letter-spacing: 3px; color: #333; }

  .edge-bar { position: absolute; right: 0; width: 7px; background: var(--navy); }
  .edge-bar--name { top: 60px; height: 29px; }
  .edge-bar--address { top: 138px; height: 35px; }
  .edge-bar--phone { top: 186px; height: 47px; }
  .edge-bar--online { top: 254px; height: 31px; }

  .person { position: absolute; right: 22px; top: 60px; font-size: 26px; font-weight: 700; color: var(--navy); }
  .info { position: absolute; right: 22px; text-align: right; font-size: 14px; line-height: 16px; }
  .info--address { top: 137px; }
  .info--online { top: 253px; }
  .phones { position: absolute; right: 22px; top: 186px; display: grid; grid-template-columns: auto auto; column-gap: 4px; font-size: 14px; line-height: 16px; }
  .phones dt { font-weight: 700; }
</style>
</head>
<body>

<section class="card card--front-light">
  <div class="front-logo"><span class="wordmark">KMayer</span></div>
  <p class="front-web">www.klaus-mayer.de</p>
</section>

<section class="card card--front-dark">
  <div class="front-logo"><span class="wordmark">KMayer</span></div>
  <p class="front-web">www.klaus-mayer.de</p>
</section>

<section class="card card--back-a">
  <span class="rule rule--top"></span>
  <span class="rule rule--bottom"></span>
  <div class="back-logo"><span class="wordmark">KMayer</span><span class="tagline">Fenster und Türen</span></div>
  <h1 class="person">Klaus Mayer</h1>
  <span class="edge-bar edge-bar--name"></span>
  <p class="info info--address">Lindenweg 12<br>79999 Talheim-Oberdorf</p>
  <span class="edge-bar edge-bar--address"></span>
  <dl class="phones">
    <dt>Mobil</dt><dd>: 0170 555 21 08</dd>
    <dt>Büro</dt><dd>: 07700 555 48 26</dd>
    <dt>Fax</dt><dd>: 03200 555 67 19</dd>
  </dl>
  <span class="edge-bar edge-bar--phone"></span>
  <p class="info info--online">mayer@email.com<br>www.klaus-mayer.de</p>
  <span class="edge-bar edge-bar--online"></span>
</section>

<section class="card card--back-b">
  <span class="rule rule--top"></span>
  <span class="rule rule--bottom"></span>
  <div class="back-logo"><span class="wordmark">KMayer</span><span class="tagline">Fenster und Türen</span></div>
  <h2 class="person">Klaus Mayer</h2>
  <span class="edge-bar edge-bar--name"></span>
  <p class="info info--address">Lindenweg 12<br>79999 Talheim-Oberdorf</p>
  <span class="edge-bar edge-bar--address"></span>
  <dl class="phones">
    <dt>Mobil</dt><dd>: 0170 555 21 08</dd>
    <dt>Büro</dt><dd>: 07700 555 48 26</dd>
    <dt>Fax</dt><dd>: 03200 555 67 19</dd>
  </dl>
  <span class="edge-bar edge-bar--phone"></span>
  <p class="info info--online">mayer@email.com<br>www.klaus-mayer.de</p>
  <span class="edge-bar edge-bar--online"></span>
</section>

</body>
</html>
```